Christmas Ballet Poster for El Relojero

I urgently need a poster for the El Relojero ballet, it needs to look magical and very similar to the reference attached. The title should be El Relojero and the typography and look should be as similar as possible as the words The Glassblower in the reference attached. Use a dancers photo just for reference, I will not use that photo as someone will be taking the picture of the principal dancer and we will be using that. It should look magical, upscale and pretty.
Requirements
Must have
- Title: El Relojero
- Space for date, time and prices
- Space to add logo
- It must look as similar as the reference as possible, magical, elegant.
Should not have
- Any logo

```html
<!DOCTYPE html>
<html lang="es">
<head>
<meta charset="utf-8">
<title>El Relojero 2018 – Ballet Poster</title>
<link rel="stylesheet" href="https://fonts.googleapis.com/css2?family=Cinzel:wght@400;600&family=Playfair+Display:wght@700;900&display=swap">
<style>
  :root {
    --night: #04060d;
    --stage: #0d1526;
    --stage-blue: #1c2c4a;
    --tutu: #9ed6dc;
    --title-light: #dcecff;
    --title-mid: #6f9be0;
    --title-deep: #1f4aa8;
    --accent: #2f5fd8;
    --white: #ffffff;
  }
  * { margin: 0; padding: 0; box-sizing: border-box; }
  html, body {
    width: 1200px; height: 584px; overflow: hidden;
    background: var(--night);
  }
  .poster {
    position: relative;
    width: 1200px; height: 584px;
    overflow: hidden;
    background: var(--night);
  }
  .stage-photo {
    position: absolute; inset: 0;
    background:
      radial-gradient(ellipse 170px 300px at 170px 300px, rgba(158,214,220,.55), rgba(158,214,220,0) 70%),
      radial-gradient(ellipse 120px 70px at 390px 400px, rgba(90,140,190,.35), rgba(90,140,190,0) 70%),
      radial-gradient(ellipse 120px 70px at 700px 400px, rgba(90,140,190,.3), rgba(90,140,190,0) 70%),
      radial-gradient(ellipse 520px 420px at 520px 330px, var(--stage-blue), rgba(13,21,38,0) 75%),
      linear-gradient(180deg, var(--night) 0%, var(--stage) 55%, var(--night) 100%);
  }
  .logo-space {
    position: absolute;
    left: 947px; top: 32px;
    width: 213px; height: 115px;
    border: 2px solid var(--accent);
    border-radius: 10px;
    background: rgba(4,6,13,.9);
    display: flex; align-items: center; justify-content: center;
    font-family: "Cinzel", serif;
    font-weight: 400;
    font-size: 50px;
    color: var(--white);
  }
  .title {
    position: absolute;
    right: 32px; top: 222px;
    font-family: "Playfair Display", serif;
    font-weight: 900;
    line-height: 1;
    white-space: nowrap;
  }
  .title-article {
    font-size: 82px;
    color: var(--title-deep);
    -webkit-text-stroke: 2px var(--title-light);
    text-shadow: 0 0 10px rgba(255,255,255,.6);
    margin-right: 10px;
  }
  .title-name {
    font-size: 118px;
    background: linear-gradient(180deg, var(--title-light) 0%, var(--title-mid) 45%, var(--title-deep) 100%);
    -webkit-background-clip: text; background-clip: text;
    color: transparent;
    -webkit-text-stroke: 1.5px var(--title-light);
    filter: drop-shadow(0 0 8px rgba(255,255,255,.75));
  }
  .year {
    position: absolute;
    right: 36px; top: 336px;
    font-family: "Playfair Display", serif;
    font-weight: 700;
    font-size: 88px;
    line-height: 1;
    color: var(--white);
  }
  .event-details {
    position: absolute;
    left: 0; right: 0; bottom: 0;
    height: 72px;
    background: linear-gradient(180deg, rgba(4,6,13,0) 0%, rgba(4,6,13,.85) 60%);
  }
  .event-details-line {
    position: absolute;
    left: 250px; top: 16px;
    font-family: "Cinzel", serif;
    font-weight: 400;
    font-size: 31px;
    color: var(--white);
    white-space: nowrap;
    display: flex; align-items: center;
  }
  .detail-divider {
    display: inline-block;
    width: 1px; height: 32px;
    background: rgba(255,255,255,.7);
    margin: 0 12px;
  }
  .rule {
    position: absolute;
    left: 0; right: 0; bottom: 10px;
    height: 2px;
    background: linear-gradient(90deg, rgba(47,95,216,0), var(--accent) 30%, var(--accent) 70%, rgba(47,95,216,0));
  }
</style>
</head>
<body>
  <div class="poster">
    <div class="stage-photo" role="img" aria-label="Stage photograph of a principal ballerina en pointe in a pale blue tutu, arms raised, with corps de ballet dancers in blue tutus in the dark background"></div>

    <div class="logo-space">Logo</div>

    <h1 class="title"><span class="title-article">El</span><span class="title-name">Relojero</span></h1>
    <div class="year">2018</div>

    <div class="event-details">
      <p class="event-details-line">
        <span>date-00/00/18</span><span class="detail-divider"></span><span>Time-00 hours</span><span class="detail-divider"></span><span>Price- $00</span>
      </p>
      <div class="rule"></div>
    </div>
  </div>
</body>
</html>
```